2 sided Handyman Postcard Design with coupon on the back

Company name is "Miles ReadyFix" Looking for a postcard that's also a business card. Showing Miles ReadyFix, 4172 Tamber Glen Rd NE, Washington C.H., Ohio 43160, 740-318-2964, dkweller@mailbrook.net coupon- $25 off any job over $100, $50 off any job over $250, $75 off any job over $500, $100 off any job over $750, qualifications, experience 25 years. No job is to small. Handyman service. home repair. Free estimates. Examples, Flooring, Cabinets, Decks, Odd Jobs, Carpentry, Painting, Drywall repair, Ceramic tile, Screen repair, fence repair, Pressure wash, Hang a Picture, wood rot repair, Plumbing, Electrical, Small Jobs, Install ceiling fan, replace garbage disposal, toilet repair, install new lighting, Install safety grab bars, caulk tub or Kitchen, Hang Blinds/rods, Replace a switch/outlet, Replace/adjust doors and locksets, replace faucets/sinks/vanity tops, And much more. Have a signature look, I wear a ranger drifton hat on the job, full beard, and glasses. Am looking for a caricature of that with tools as main logo which should be shown on front and the back. One year warranty, Bonded, Insured. Cash or checks

```html
<!DOCTYPE html>
<html lang="en">
<head>
<meta charset="utf-8">
<title>Miles ReadyFix Handyman Postcard</title>
<link href="https://fonts.googleapis.com/css2?family=Roboto+Slab:wght@800;900&family=Arimo:wght@400;700&family=Anton&family=Lora:wght@500&family=Playfair+Display:ital,wght@0,700;1,700&display=swap" rel="stylesheet">
<style>
:root{
  --stage:#3a3a3a;
  --navy:#223e8c;
  --navy-deep:#1b2f72;
  --orange:#f05a24;
  --orange-hot:#e8401c;
  --orange-soft:#f47a2c;
  --yellow:#ffe11a;
  --white:#ffffff;
  --swoosh:#aab6d6;
  --coupon-red:#e3141f;
  --ink:#111111;
}
*{margin:0;padding:0;box-sizing:border-box}
html,body{width:1029px;height:1200px;overflow:hidden;background:var(--stage)}
.card{position:absolute;left:138px;width:750px;height:581px;background:var(--navy);overflow:hidden;font-family:"Arimo",Arial,sans-serif;color:var(--white)}
.card--front{top:9px}
.card--back{top:605px}
.card-bg{position:absolute;inset:0}
.mascot{position:absolute;border-radius:40% 40% 20% 20%;background:linear-gradient(180deg,#8a6a45 0%,#e5b48a 25%,#2f63c6 55%,#23479a 85%,#6b4a2e 100%);opacity:.9}
.brand-name{position:absolute;font-family:"Roboto Slab",Georgia,serif;font-weight:900;letter-spacing:0;color:var(--white);white-space:nowrap;line-height:1}
.tagline{position:absolute;left:192px;top:84px;font-family:"Lora",Georgia,serif;font-weight:500;font-size:27px;line-height:1.1;color:var(--yellow)}
.estimate-badge{position:absolute;left:568px;top:28px;width:150px;height:130px;border-radius:50% 45% 40% 55%;background:linear-gradient(160deg,#ffffff 0%,#ffe2cf 40%,#f26a22 70%,#f5c518 100%)}
.services-title{position:absolute;left:235px;top:163px;font-size:23px;line-height:1;font-weight:700;color:var(--orange-soft);letter-spacing:.2px}
.service-col{position:absolute;top:192px;list-style:none;font-size:13.2px;font-weight:700;line-height:18px;white-space:nowrap}
.service-col li::before{content:"";display:inline-block;width:3px;height:3px;background:var(--orange-hot);margin:0 3px 3px 0;vertical-align:middle}
.col-a{left:237px}.col-b{left:344px}.col-c{left:490px}
.motto{position:absolute;left:301px;top:363px;font-family:"Roboto Slab",Georgia,serif;font-weight:800;font-size:24px;line-height:1.1}
.call-line{position:absolute;left:276px;top:388px;font-family:"Anton",Impact,sans-serif;font-size:42px;line-height:1.1;color:var(--orange-hot);white-space:nowrap;letter-spacing:-.5px}
.call-line svg{vertical-align:middle;margin-right:2px}
.address-block{position:absolute;left:39px;top:488px;font-size:17px;font-weight:700;line-height:18px}
.address-block .label{font-weight:400;color:var(--ink)}
.email-line{position:absolute;left:336px;top:520px;font-size:21px;display:flex;align-items:center;gap:8px}
.turn-note{position:absolute;left:666px;top:528px;transform:rotate(-45deg);font-size:11px;font-weight:700;color:var(--ink);text-align:center;line-height:12px}
.back-address{position:absolute;left:63px;top:68px;font-size:17px;line-height:1.1;font-weight:700;color:var(--yellow);white-space:nowrap}
.trust-text{position:absolute;left:561px;top:52px;width:150px;text-align:center;font-family:"Roboto Slab",Georgia,serif;font-weight:800;font-size:20px;line-height:22px}
.experience{position:absolute;left:222px;top:146px;font-size:21px;line-height:1.2;white-space:nowrap}
.experience b{font-family:"Anton",Impact,sans-serif;font-weight:400;font-size:28px;line-height:1;color:var(--yellow);font-style:italic}
.coupons{position:absolute;left:301px;top:190px;width:388px;height:249px;background:var(--white);display:grid;grid-template-columns:1fr 1fr;grid-template-rows:1fr 1fr;border:2px dashed #222;outline:4px solid var(--white)}
.coupon{border:1px dashed #222;display:flex;flex-direction:column;align-items:center;justify-content:center;gap:6px;color:var(--coupon-red);overflow:hidden}
.coupon-value{font-family:"Playfair Display",Georgia,serif;font-weight:700;display:flex;align-items:flex-end;font-variant-numeric:lining-nums}
.coupon-value .amt{font-size:60px;line-height:1;letter-spacing:-2px}
.coupon-value .unit{display:flex;flex-direction:column;color:var(--ink);font-size:26px;line-height:1;margin:0 0 6px 2px}
.coupon-value .unit span:first-child{font-size:22px}
.coupon-terms{background:var(--navy-deep);color:var(--white);font-family:"Playfair Display",Georgia,serif;font-size:13px;line-height:17px;padding:0 18px;font-weight:400;white-space:nowrap;font-variant-numeric:lining-nums}
.coupon-terms i{color:var(--yellow);font-weight:700}
.payment-tag{position:absolute;left:448px;top:466px;width:302px;height:48px;background:var(--ink);clip-path:polygon(22px 0,100% 0,100% 100%,22px 100%,0 50%);font-family:"Roboto Slab",Georgia,serif;font-weight:800;font-size:23px;display:flex;align-items:center;padding-left:32px;white-space:nowrap}
.call-today{position:absolute;left:33px;top:517px;font-family:"Anton",Impact,sans-serif;font-size:32px;line-height:1.1;white-space:nowrap;letter-spacing:-.5px}
.call-today .phone{color:var(--navy);font-size:38px}
.back-email{position:absolute;left:430px;top:530px;font-size:21px;line-height:1.2;white-space:nowrap}
</style>
</head>
<body>

<section class="card card--front">
  <svg class="card-bg" viewBox="0 0 750 581" aria-hidden="true">
    <defs>
      <linearGradient id="frontOrange" x1="0" y1="0" x2="1" y2="0">
        <stop offset="0" stop-color="#e8401c"/><stop offset=".6" stop-color="#f05a24"/><stop offset="1" stop-color="#f47a2c"/>
      </linearGradient>
    </defs>
    <path d="M0 360 C140 380 300 470 500 478 C610 482 690 450 750 420 L750 581 L0 581Z" fill="#ffffff"/>
    <path d="M0 378 C140 398 300 488 500 494 C610 498 690 468 750 440 L750 581 L0 581Z" fill="url(#frontOrange)"/>
    <path d="M212 200 C250 155 420 132 530 146 C420 142 280 160 228 208Z" fill="var(--swoosh)"/>
    <path d="M560 400 C640 412 680 440 660 460 C630 478 520 480 400 470 C520 470 620 462 640 446 C652 432 620 414 560 400Z" fill="var(--swoosh)"/>
    <path d="M604 581 L750 465 L750 581Z" fill="#ffffff"/>
    <path d="M604 581 C640 520 690 480 750 465 C700 500 690 540 690 581Z" fill="#d8d8d8"/>
    <path d="M636 484 L656 504 L661 496 L664 518 L642 515 L650 510 L630 490Z" fill="#4f8fa6"/>
  </svg>

  <div class="mascot" style="left:40px;top:24px;width:196px;height:420px" role="img" aria-label="Caricature mascot of a bearded handyman in a brown hat and glasses, wearing blue overalls, giving a thumbs up and carrying a red toolbox"></div>

  <h1 class="brand-name" style="left:192px;top:44px;font-size:34px">MILES READYFIX</h1>
  <p class="tagline">Handyman Service</p>
  <div class="estimate-badge" role="img" aria-label="Hand-lettered orange Free Estimates badge"></div>

  <h2 class="services-title">SERVICES INCLUDES</h2>
  <ul class="service-col col-a">
    <li>Flooring,</li><li>Cabinets,</li><li>Decks,</li><li>Odd Jobs,</li><li>Carpentry,</li><li>Painting,</li><li>Drywall repair,</li><li>Ceramic tile,</li>
  </ul>
  <ul class="service-col col-b">
    <li>Screen repair,</li><li>Fence repair,</li><li>Pressure wash,</li><li>Hang a Picture,</li><li>wood rot repair,</li><li>Plumbing, Electrical,</li><li>Small Jobs,</li><li>Install ceiling fan,</li><li>Toilet repair,</li>
  </ul>
  <ul class="service-col col-c">
    <li>Replace garbage disposal,</li><li>Install new lighting,</li><li>Install safety grab bars,</li><li>Caulk tub or Kitchen,</li><li>Hang Blinds/rods,</li><li>Replace a switch/outlet,</li><li>Replace/adjust doors and locksets,</li><li>Replace faucets/sinks/vanity tops,</li><li>And much more</li>
  </ul>

  <p class="motto">NO JOB IS TOO SMALL</p>
  <p class="call-line"><svg width="16" height="34" viewBox="0 0 16 34" aria-hidden="true"><path d="M12 2 C4 6 2 14 3 20 C4 26 8 31 13 32 L15 27 C11 26 9 22 9 17 C9 12 11 9 14 7Z" fill="#ffffff"/></svg>CALL - 740-318-2964</p>

  <div class="address-block">
    <span class="label">Address</span><br>
    4172 Tamber Glen Rd NE,<br>
    Washington C.H., Ohio 43160
  </div>
  <p class="email-line">
    <svg width="30" height="20" viewBox="0 0 30 20" aria-hidden="true"><rect x="1" y="1" width="28" height="18" fill="none" stroke="#1b1b1b" stroke-width="2"/><path d="M1 1 L15 12 L29 1 M1 19 L11 9 M29 19 L19 9" fill="none" stroke="#1b1b1b" stroke-width="2"/></svg>
    dkweller@mailbrook.net
  </p>
  <p class="turn-note">TURN FOR<br>OFFERS</p>
</section>

<section class="card card--back">
  <svg class="card-bg" viewBox="0 0 750 581" aria-hidden="true">
    <defs>
      <linearGradient id="backOrange" x1="0" y1="0" x2="1" y2="0">
        <stop offset="0" stop-color="#e8401c"/><stop offset=".6" stop-color="#f05a24"/><stop offset="1" stop-color="#f47a2c"/>
      </linearGradient>
    </defs>
    <path d="M0 380 C150 410 330 470 520 470 C620 470 700 455 750 440 L750 581 L0 581Z" fill="#ffffff"/>
    <path d="M0 396 C150 426 330 486 520 486 C620 486 700 470 750 456 L750 581 L0 581Z" fill="url(#backOrange)"/>
    <path d="M205 184 C240 134 420 116 520 124 C420 126 270 144 222 190Z" fill="var(--swoosh)"/>
    <path d="M598 33 L674 33 L711 63 L711 107 L674 137 L598 137 L561 107 L561 63Z" fill="var(--orange)" stroke="#ffffff" stroke-width="3"/>
  </svg>

  <h1 class="brand-name" style="left:63px;top:32px;font-size:34px">MILES READYFIX</h1>
  <p class="back-address">4172 Tamber Glen Rd NE,Washington C.H.Ohio 43160</p>
  <p class="trust-text">BONDED<br>&amp;<br>INSURED</p>

  <div class="mascot" style="left:34px;top:100px;width:200px;height:410px" role="img" aria-label="Caricature mascot of a bearded handyman in a brown hat and glasses, wearing blue overalls, giving a thumbs up and carrying a red toolbox"></div>

  <p class="experience">QUALIFICATIONS, EXPERIENCE <b>25</b> YEARS</p>

  <div class="coupons">
    <div class="coupon">
      <div class="coupon-value"><span class="amt">25</span><span class="unit"><span>$</span><span>OFF</span></span></div>
      <div class="coupon-terms">Any Job Over <i>$100</i></div>
    </div>
    <div class="coupon">
      <div class="coupon-value"><span class="amt">50</span><span class="unit"><span>$</span><span>OFF</span></span></div>
      <div class="coupon-terms">Any Job Over <i>$250</i></div>
    </div>
    <div class="coupon">
      <div class="coupon-value"><span class="amt">75</span><span class="unit"><span>$</span><span>OFF</span></span></div>
      <div class="coupon-terms">Any Job Over <i>$500</i></div>
    </div>
    <div class="coupon">
      <div class="coupon-value"><span class="amt">100</span><span class="unit"><span>$</span><span>OFF</span></span></div>
      <div class="coupon-terms">Any Job Over <i>$750</i></div>
    </div>
  </div>

  <div class="payment-tag">CASH OR CHEQUE</div>
  <p class="call-today">CALL TODAY - <span class="phone">740-318-2964</span></p>
  <p class="back-email">Email - dkweller@mailbrook.net</p>
</section>

</body>
</html>
```